Design wireframe of E-commerce website *

We are a European online shoe store located in Sweden. The project is to redesign the first page of our e-commerce website https://kelvaro.se/skor
We want to receive creative ideas of what our website could look like while keeping all the functions and flows. The new design should be simple, lean and modern.
Specifications:
We have several guidelines for what we are expecting
- Redesign the frontend of our website first page https://kelvaro.se/skor and the child page https://www.kelvaro.se/skor/dam
- You need to provide a complete clickable wireframe of the target pages.
- All existing components should be in the new design.
- The pages should include all sections: header, footer, product lists and widgets. The page structure of the site should look as the example: https://www.trimsel.co.uk/shoes
- The design must be responsive and Mobile First which can be read from all browsers and different devices.
- You need to have in mind that we really want it to be mobile first, meaning
the mobile view is the most important one
- The new design should reflect our brands essence and come along with the new brandprofiles (fonts, icons...). For example http://brandprofile.trimsel.com/, but keep the logo and colour of the existing Kelvaro theme.
- The design should be user friendly.
- The design should be simple enough that the pages can be downloaded fast.
- The new design should look fashionable and be able to generating attracting
traffic.
- The text on the child page https://www.kelvaro.se/skor/dam should be handled in a better way and make it easier for users to know which page they are looking at. You can see the example at https://www.trimsel.co.uk/shoes/women but we are open to your good ideas as well.
- We do not want shelves in the design. Trimsel has it, but Kelvaro
should not.
- We want to keep the existing responsive sizes for product list which means 2, 4 or 6 pairs of shoes per row.
Practical Information:
We are located in Sweden and have working hours between 9:00 -12:00 (CEST)
Monday - Friday. We have limited capacity to answer every question you have
but will try to get back to you in our working hours as much as we can then
hopefully this can help you get a better understanding of what we are
looking for.
Future Possibilities:We are going to redesign the whole site
of https://www.kelvaro.se/skor so the winner
will have the chance to do all the pages in the near future. We are
actively seeking designers for future collaborations on a long-term basis
and it is possible to create a partnership if your work is impressive
enough. *

```html
<!DOCTYPE html>
<html lang="sv">
<head>
<meta charset="utf-8">
<title>Kelvaro – Skor</title>
<link href="https://fonts.googleapis.com/css2?family=Roboto:wght@300;400;500;700&family=Montserrat:wght@700;800&display=swap" rel="stylesheet">
<style>
:root{
  --purple:#5b1a9a;
  --purple-light:#b99ad8;
  --ink:#222;
  --muted:#777;
  --line:#e4e4e4;
  --black:#111;
  --footer:#2b2b2b;
  --footer-deep:#1f1f1f;
  --page:#ededee;
  --white:#fff;
  --soft:#f4f4f5;
  --sea1:#3cb7c9;
  --sea2:#62cbd6;
  --skin1:#d9c2b3;
  --skin2:#efe6e0;
}
*{box-sizing:border-box;margin:0;padding:0}
html,body{width:1200px;height:4455px;overflow:hidden}
body{background:var(--page);font-family:'Roboto',sans-serif;color:var(--ink);position:relative}

.site{position:absolute;background:var(--white);overflow:hidden}
.site--desktop{left:48px;top:0;width:767px;height:2240px}
.site--mobile{left:891px;top:45px;width:244px;height:4235px}

/* header */
.header{display:flex;align-items:center;justify-content:space-between;border-bottom:1px solid var(--line);font-size:9px;color:var(--muted)}
.site--desktop .header{height:80px;padding:0 40px}
.site--mobile .header{height:68px;padding:0 10px;flex-wrap:wrap}
.header-tools{display:flex;gap:14px;align-items:center}
.tool{display:flex;align-items:center;gap:4px}
.tool svg{width:12px;height:12px}
.logo{font-family:'Montserrat',sans-serif;font-weight:800;color:var(--black);letter-spacing:1px}
.site--desktop .logo{font-size:22px}
.site--mobile .logo{font-size:16px;width:100%;text-align:center;padding-top:6px}

/* hero */
.hero{position:relative;background:linear-gradient(180deg,var(--sea1),var(--sea2) 60%,#d9c7a8);display:flex;flex-direction:column;align-items:center;justify-content:center;color:var(--white)}
.site--desktop .hero{height:200px}
.site--mobile .hero{height:282px}
.hero-title{font-weight:500;text-align:center;letter-spacing:1px}
.site--desktop .hero-title{font-size:26px}
.site--mobile .hero-title{font-size:24px;line-height:1.2}
.btn{background:var(--purple);color:var(--white);font-size:8px;font-weight:700;padding:5px 14px;margin-top:8px;letter-spacing:1px}
.arrow{position:absolute;top:50%;width:18px;height:18px;border-radius:50%;background:var(--black);display:flex;align-items:center;justify-content:center;transform:translateY(-50%)}
.arrow--l{left:12px}.arrow--r{right:12px}
.arrow svg{width:8px;height:8px}

/* categories */
.categories{display:grid;gap:8px}
.site--desktop .categories{grid-template-columns:repeat(7,1fr);margin:28px 60px 0;gap:8px}
.site--mobile .categories{grid-template-columns:repeat(2,1fr);margin:8px 12px 0;gap:8px}
.cat{border:1px solid var(--line);background:var(--white);display:flex;flex-direction:column;align-items:center;font-size:6px;text-transform:uppercase;color:var(--muted)}
.cat--active{background:var(--purple);color:var(--white);border-color:var(--purple)}
.cat-img{width:70%;margin:6px 0 4px;border-radius:2px}
.site--desktop .cat{height:70px}.site--desktop .cat-img{height:40px}
.site--mobile .cat{height:106px}.site--mobile .cat-img{height:70px;margin-top:10px}

/* promo */
.photo-run{background:linear-gradient(135deg,var(--skin2),var(--skin1) 55%,#f7f7f7)}
.photo-sea{background:linear-gradient(135deg,var(--sea1),#8fd8df 50%,#e9c6c2)}
.framed{position:relative}
.framed .frame{position:absolute;border:6px solid var(--purple)}
.framed .frame--black{border-color:var(--black)}
.promo-box{color:var(--white);font-size:9px;line-height:1.5;letter-spacing:1px;text-transform:uppercase;outline:1px solid var(--line);outline-offset:3px}
.promo-box--purple{background:var(--purple)}
.promo-box--black{background:var(--black)}

/* section titles */
.section-title{display:flex;align-items:center;justify-content:center;color:var(--purple);font-size:12px}
.section-title span{padding:0 10px;border-left:1px solid var(--line);border-right:1px solid var(--line)}
.rule{height:1px;background:var(--line)}

/* products */
.products{display:flex;justify-content:center}
.product{position:relative;width:128px;height:158px;text-align:center}
.product svg.shape{position:absolute;inset:0}
.product-img{position:relative;width:88px;height:50px;margin:14px auto 6px;border-radius:2px}
.product-name{position:relative;font-size:8px;font-weight:500}
.product-sub{position:relative;font-size:5px;color:var(--muted);margin-top:2px}
.product-price{position:relative;font-size:13px;font-weight:700;margin-top:6px}
.product-price s{font-size:7px;color:#d33;font-weight:400;margin-left:4px}
.dots{display:flex;justify-content:center;gap:6px}
.dot{width:12px;height:12px;border-radius:50%;background:var(--black);color:var(--white);font-size:7px;display:flex;align-items:center;justify-content:center}
.dot--on{background:var(--purple)}

/* news */
.news{position:relative;text-align:center}
.news-date{font-size:10px;font-weight:500}
.news-text{font-size:5.5px;color:var(--muted);line-height:1.6;margin:8px auto 0}
.news-icon{width:14px;height:14px;margin:10px auto 0;border-radius:3px;background:linear-gradient(135deg,#8bc34a,#ffc107 50%,#7e57c2)}
.news .arrow{background:var(--purple)}

/* nav & brands */
.foot-nav{display:grid;gap:6px;font-size:6px;color:var(--ink)}
.foot-nav a{border:1px solid var(--line);height:18px;display:flex;align-items:center;justify-content:center;text-decoration:none;color:inherit}
.brands{display:flex;align-items:center}
.brand{font-weight:700;font-size:17px;color:var(--black);display:flex;align-items:center;gap:6px}
.brand i{display:block;width:8px;height:8px;background:var(--black)}

/* newsletter */
.newsletter{background:var(--soft);text-align:center;position:relative}
.nl-ghost{color:#e2e2e4;font-weight:700;white-space:nowrap}
.nl-title{position:absolute;left:0;right:0;color:var(--purple)}
.nl-input{background:var(--white);border:1px solid var(--line);height:16px;font-size:5px;color:#aaa;text-align:left;padding:5px 6px;margin:0 auto}
.features{display:flex;justify-content:center}
.feature{background:var(--white);display:flex;flex-direction:column;align-items:center;justify-content:center;font-size:5.5px;color:var(--ink)}
.feature svg{width:24px;height:24px;margin-bottom:6px}

/* footer */
.footer{background:var(--footer);color:#bbb;font-size:6px;line-height:1.8}
.footer h4{color:var(--white);font-size:6px;font-weight:700;letter-spacing:.5px;margin-bottom:4px}
.footer-top{display:flex;justify-content:flex-end;gap:20px;border-bottom:1px solid #3d3d3d}
.socials{display:flex;gap:5px;margin-top:3px}
.socials span{width:12px;height:12px;border:1px solid #888;border-radius:50%}
.copyright{background:var(--white);font-size:5.5px;color:var(--muted);text-align:center}
</style>
</head>
<body>

<!-- ================= DESKTOP ================= -->
<main class="site site--desktop">
  <header class="header">
    <div class="header-tools">
      <span class="tool"><svg viewBox="0 0 12 12"><path d="M1 3h10M1 6h10M1 9h10" stroke="#555" stroke-width="1.2"/></svg>Meny</span>
      <span class="tool"><svg viewBox="0 0 12 12"><circle cx="5" cy="5" r="3.5" fill="none" stroke="#555"/><path d="M8 8l3 3" stroke="#555"/></svg>Sök här</span>
    </div>
    <div class="logo">KELVARO</div>
    <div class="header-tools">
      <span class="tool"><svg viewBox="0 0 12 12"><path d="M1 2h2l1.5 6h6l1-4H4" fill="none" stroke="#555"/></svg>Varukorg</span>
      <span class="tool"><svg viewBox="0 0 12 12"><path d="M6 10L1.5 5.5A2.5 2.5 0 016 2.5a2.5 2.5 0 014.5 3z" fill="none" stroke="#555"/></svg>Önskelista</span>
    </div>
  </header>

  <section class="hero" role="img" aria-label="Rad av färgglada damskor mot turkos trävägg">
    <h1 class="hero-title">TUSENTALS SKOR 50%- PA</h1>
    <span class="btn">SHOP NOW</span>
    <span class="arrow arrow--l"><svg viewBox="0 0 8 8"><path d="M5 1L2 4l3 3" stroke="#fff" fill="none"/></svg></span>
    <span class="arrow arrow--r"><svg viewBox="0 0 8 8"><path d="M3 1l3 3-3 3" stroke="#fff" fill="none"/></svg></span>
  </section>

  <nav class="categories">
    <div class="cat cat--active"><div class="cat-img" style="background:#c9b2e0" role="img" aria-label="Sportsko"></div>Sportskor</div>
    <div class="cat"><div class="cat-img" style="background:#d8d8d8" role="img" aria-label="Sneaker"></div>Sneakers</div>
    <div class="cat"><div class="cat-img" style="background:#c9b08e" role="img" aria-label="Pump"></div>Pumps</div>
    <div class="cat"><div class="cat-img" style="background:#e8a3b3" role="img" aria-label="Sandal"></div>Sandaler</div>
    <div class="cat"><div class="cat-img" style="background:#6b4a3c" role="img" aria-label="Känga"></div>Kängor</div>
    <div class="cat"><div class="cat-img" style="background:#d9b9a7" role="img" aria-label="Klack"></div>Klackskor</div>
    <div class="cat"><div class="cat-img" style="background:#b8906f" role="img" aria-label="Boots"></div>Boots</div>
    <div class="cat"><div class="cat-img" style="background:#8b6a55" role="img" aria-label="Loafer"></div>Loafers</div>
    <div class="cat"><div class="cat-img" style="background:#2c3a66" role="img" aria-label="Stövel"></div>Stövlar</div>
    <div class="cat"><div class="cat-img" style="background:#333" role="img" aria-label="Finsko"></div>Finskor</div>
    <div class="cat"><div class="cat-img" style="background:#e0468e" role="img" aria-label="Ballerina"></div>Ballerina</div>
    <div class="cat"><div class="cat-img" style="background:#4a2a22" role="img" aria-label="Sko"></div>Herr</div>
    <div class="cat"><div class="cat-img" style="background:#9c7a5b" role="img" aria-label="Sandal"></div>Barn</div>
    <div class="cat"><div class="cat-img" style="background:#c4a87a" role="img" aria-label="Tofflor"></div>Tofflor</div>
  </nav>

  <section style="position:relative;height:290px;margin-top:30px">
    <div class="photo-run" role="img" aria-label="Person som knyter sina vita sneakers" style="position:absolute;left:110px;top:0;width:220px;height:275px"></div>
    <div class="framed" style="position:absolute;left:358px;top:10px;width:268px;height:145px">
      <div class="frame" style="left:40px;top:-8px;right:-8px;bottom:40px"></div>
      <div class="photo-sea" role="img" aria-label="Färgglada skor på turkos bakgrund" style="position:absolute;inset:8px 20px 0 0"></div>
    </div>
    <div class="promo-box promo-box--purple" style="position:absolute;left:362px;top:178px;width:142px;height:96px;padding:14px 12px">- Sandler<br>Finskor -<br>&nbsp;&nbsp;- Klackskor<br>Stövlar -</div>
    <div class="promo-box promo-box--black" style="position:absolute;left:520px;top:178px;width:142px;height:96px;padding:14px 12px">- Sandler<br>Finskor -<br>&nbsp;&nbsp;- Klackskor<br>Stövlar -</div>
  </section>

  <h2 class="section-title" style="margin-top:28px"><span>Products</span></h2>
  <div class="products" style="gap:30px;margin-top:20px">
    <article class="product"><svg class="shape" viewBox="0 0 128 158"><polygon points="1,1 127,1 127,128 64,157 1,128" fill="#fff" stroke="#b99ad8"/></svg><div class="product-img" style="background:#e2337d" role="img" aria-label="Rosa sportsko"></div><div class="product-name">Sportskor</div><div class="product-sub">Vintage lätt sko</div><div class="product-price">325kr<s>450kr</s></div></article>
    <article class="product"><svg class="shape" viewBox="0 0 128 158"><polygon points="1,1 127,1 127,128 64,157 1,128" fill="#fff" stroke="#b99ad8"/></svg><div class="product-img" style="background:#d9b690" role="img" aria-label="Beige sandal med klack"></div><div class="product-name">Sandlar</div><div class="product-sub">Vintage lätt sko</div><div class="product-price">325kr<s>450kr</s></div></article>
    <article class="product"><svg class="shape" viewBox="0 0 128 158"><polygon points="1,1 127,1 127,128 64,157 1,128" fill="#fff" stroke="#b99ad8"/></svg><div class="product-img" style="background:#2e3b63" role="img" aria-label="Marinblå stövel"></div><div class="product-name">Stövlar</div><div class="product-sub">Vintage lätt sko</div><div class="product-price">325kr<s>450kr</s></div></article>
    <article class="product"><svg class="shape" viewBox="0 0 128 158"><polygon points="1,1 127,1 127,128 64,157 1,128" fill="#fff" stroke="#b99ad8"/></svg><div class="product-img" style="background:#7e57c2" role="img" aria-label="Lila sneaker"></div><div class="product-name">Loafer</div><div class="product-sub">Vintage lätt sko</div><div class="product-price">325kr<s>450kr</s></div></article>
  </div>
  <div class="dots" style="margin-top:22px"><span class="dot dot--on">1</span><span class="dot">2</span></div>

  <div class="rule" style="margin:40px 110px 0"></div>
  <h2 class="section-title" style="margin-top:34px"><span>News</span></h2>
  <section class="news" style="margin:18px 110px 0;padding:12px 30px 0;height:95px">
    <div class="news-date">21 Maj 2018</div>
    <p class="news-text" style="width:440px">Nya säsongen är här med lätta sneakers, sandaler och klackskor i vårens färger. Upptäck våra nyheter och hitta skor för varje tillfälle, från vardag till fest. Fri frakt och fri retur på alla beställningar, samt trettio dagars öppet köp för alla kunder i hela Sverige och Europa.</p>
    <div class="news-icon" role="img" aria-label="Nyhetsikon"></div>
    <span class="arrow arrow--l" style="left:0;top:30px"><svg viewBox="0 0 8 8"><path d="M5 1L2 4l3 3" stroke="#fff" fill="none"/></svg></span>
    <span class="arrow arrow--r" style="right:0;top:30px"><svg viewBox="0 0 8 8"><path d="M3 1l3 3-3 3" stroke="#fff" fill="none"/></svg></span>
  </section>

  <div class="rule" style="margin:40px 110px 0"></div>
  <h2 class="section-title" style="margin-top:34px"><span>Favorites</span></h2>
  <section style="position:relative;height:150px;margin-top:22px">
    <div class="framed" style="position:absolute;left:110px;top:0;width:240px;height:140px">
      <div class="frame" style="left:30px;top:0;right:0;bottom:40px"></div>
      <div class="photo-run" role="img" aria-label="Person som knyter vita sneakers" style="position:absolute;left:0;top:18px;right:18px;bottom:0"></div>
    </div>
    <div class="framed" style="position:absolute;left:408px;top:0;width:240px;height:140px">
      <div class="frame frame--black" style="left:30px;top:0;right:0;bottom:40px"></div>
      <div class="photo-sea" role="img" aria-label="Färgglada skor på turkos bakgrund" style="position:absolute;left:0;top:18px;right:18px;bottom:0"></div>
    </div>
  </section>

  <nav class="foot-nav" style="grid-template-columns:repeat(7,1fr);margin:42px 110px 0">
    <a>Hem</a><a>Om oss</a><a>Produkter</a><a>Kategorier</a><a>Favoriter</a><a>Nyheter</a><a>Kontakt</a>
  </nav>
  <div class="brands" style="justify-content:space-between;margin:30px 130px 0">
    <span class="brand"><i></i>Arvena</span><span class="brand">Solvik</span><span class="brand">Mudlo</span><span class="brand">TAVIK</span>
  </div>

  <section class="newsletter" style="margin-top:32px;height:232px;padding-top:18px">
    <div class="nl-ghost" style="font-size:28px">Newsletter Subscribe</div>
    <div class="nl-title" style="top:28px;font-size:12px">Subscribe Newsletter</div>
    <div class="nl-input" style="width:380px;margin-top:10px">E-post</div>
    <div class="features" style="gap:14px;margin-top:22px">
      <div class="feature" style="width:160px;height:90px"><svg viewBox="0 0 24 24"><circle cx="12" cy="10" r="6" fill="none" stroke="#5b1a9a" stroke-width="1.5"/><path d="M8 15l-2 7 6-3 6 3-2-7" fill="none" stroke="#5b1a9a" stroke-width="1.5"/></svg>30 dagars öppet köp</div>
      <div class="feature" style="width:160px;height:90px"><svg viewBox="0 0 24 24"><path d="M2 5h4l3 10h10l2-7H7" fill="none" stroke="#5b1a9a" stroke-width="1.5"/><circle cx="10" cy="19" r="1.5" fill="#5b1a9a"/><circle cx="17" cy="19" r="1.5" fill="#5b1a9a"/></svg>Fri frakt och fri retur</div>
      <div class="feature" style="width:160px;height:90px"><svg viewBox="0 0 24 24"><rect x="3" y="8" width="18" height="13" fill="none" stroke="#5b1a9a" stroke-width="1.5"/><path d="M3 8l4-5h10l4 5M12 3v18" fill="none" stroke="#5b1a9a" stroke-width="1.5"/></svg>Prisgaranti</div>
    </div>
  </section>

  <footer class="footer" style="height:163px">
    <div class="footer-top" style="padding:8px 110px 6px"><span>☏ +46 8 555 0142</span><span>✉ kundtjanst@kelvaro.se</span></div>
    <div style="display:flex;gap:100px;padding:14px 110px 0">
      <div><h4>CONTACT US</h4>Skovägen 12, Kelvaro AB<br>411 08 Göteborg<br>Telefon: +46 8 555 0142<br>E-post: kundtjanst@kelvaro.se</div>
      <div><h4>USEFUL LINKS</h4>Vanliga frågor<br>Leveransvillkor<br>Retur &amp; byte<br>Storleksguide</div>
      <div><h4>&nbsp;</h4>Om Kelvaro<br>Jobb<br>Villkor</div>
      <div><h4>FOLLOW US</h4><div class="socials"><span></span><span></span><span></span></div></div>
    </div>
  </footer>
  <div class="copyright" style="padding:10px 0">© 2018 Kelvaro AB · Integritetspolicy · Användarvillkor · Cookies · Kontakt</div>
</main>

<!-- ================= MOBILE ================= -->
<main class="site site--mobile">
  <header class="header">
    <div class="logo">KELVARO</div>
    <div class="header-tools" style="gap:8px">
      <span class="tool"><svg viewBox="0 0 12 12"><path d="M1 3h10M1 6h10M1 9h10" stroke="#555" stroke-width="1.2"/></svg>Meny</span>
      <span class="tool"><svg viewBox="0 0 12 12"><circle cx="5" cy="5" r="3.5" fill="none" stroke="#555"/><path d="M8 8l3 3" stroke="#555"/></svg>Sök</span>
    </div>
    <div class="header-tools" style="gap:8px">
      <span class="tool"><svg viewBox="0 0 12 12"><path d="M1 2h2l1.5 6h6l1-4H4" fill="none" stroke="#555"/></svg>Korg</span>
      <span class="tool"><svg viewBox="0 0 12 12"><path d="M6 10L1.5 5.5A2.5 2.5 0 016 2.5a2.5 2.5 0 014.5 3z" fill="none" stroke="#555"/></svg>Önskelista</span>
    </div>
  </header>

  <section class="hero" role="img" aria-label="Rad av färgglada damskor mot turkos trävägg">
    <h1 class="hero-title">TUSENTALS<br>SKOR 50%- PA</h1>
    <span class="btn">SHOP NOW</span>
  </section>

  <nav class="categories">
    <div class="cat cat--active"><div class="cat-img" style="background:#c9b2e0" role="img" aria-label="Sportsko"></div>Sportskor</div>
    <div class="cat"><div class="cat-img" style="background:#d8d8d8" role="img" aria-label="Sneaker"></div>Sneakers</div>
    <div class="cat"><div class="cat-img" style="background:#6b4a3c" role="img" aria-label="Känga"></div>Kängor</div>
    <div class="cat"><div class="cat-img" style="background:#d9b9a7" role="img" aria-label="Klack"></div>Klackskor</div>
    <div class="cat"><div class="cat-img" style="background:#8b6a55" role="img" aria-label="Loafer"></div>Loafers</div>
    <div class="cat"><div class="cat-img" style="background:#2c3a66" role="img" aria-label="Stövel"></div>Stövlar</div>
    <div class="cat"><div class="cat-img" style="background:#333" role="img" aria-label="Finsko"></div>Finskor</div>
    <div class="cat"><div class="cat-img" style="background:#e0468e" role="img" aria-label="Ballerina"></div>Ballerina</div>
    <div class="cat"><div class="cat-img" style="background:#9c7a5b" role="img" aria-label="Sandal"></div>Sandaler</div>
    <div class="cat"><div class="cat-img" style="background:#c4a87a" role="img" aria-label="Tofflor"></div>Tofflor</div>
  </nav>

  <div class="photo-run" role="img" aria-label="Person som knyter sina vita sneakers" style="margin:15px 12px 0;height:297px"></div>
  <div class="framed" style="margin:15px 12px 0;height:163px">
    <div class="frame" style="left:30px;top:0;right:0;bottom:40px"></div>
    <div class="photo-sea" role="img" aria-label="Färgglada skor på turkos bakgrund" style="position:absolute;left:0;top:14px;right:14px;bottom:0"></div>
  </div>
  <div class="promo-box promo-box--purple" style="margin:15px 14px 0;height:103px;padding:14px 14px">- Sandler<br>Finskor -<br>&nbsp;&nbsp;- Klackskor<br>Stövlar -</div>
  <div class="promo-box promo-box--black" style="margin:15px 14px 0;height:103px;padding:14px 14px">- Sandler<br>Finskor -<br>&nbsp;&nbsp;- Klackskor<br>Stövlar -</div>

  <h2 class="section-title" style="margin-top:50px"><span>Products</span></h2>
  <div class="products" style="flex-direction:column;align-items:center;gap:24px;margin-top:20px">
    <article class="product"><svg class="shape" viewBox="0 0 128 158"><polygon points="1,1 127,1 127,128 64,157 1,128" fill="#fff" stroke="#b99ad8"/></svg><div class="product-img" style="background:#e2337d" role="img" aria-label="Rosa sportsko"></div><div class="product-name">Sportskor</div><div class="product-sub">Vintage lätt sko</div><div class="product-price">325kr<s>450kr</s></div></article>
    <article class="product"><svg class="shape" viewBox="0 0 128 158"><polygon points="1,1 127,1 127,128 64,157 1,128" fill="#fff" stroke="#b99ad8"/></svg><div class="product-img" style="background:#d9b690" role="img" aria-label="Beige sandal med klack"></div><div class="product-name">Sandlar</div><div class="product-sub">Vintage lätt sko</div><div class="product-price">325kr<s>450kr</s></div></article>
    <article class="product"><svg class="shape" viewBox="0 0 128 158"><polygon points="1,1 127,1 127,128 64,157 1,128" fill="#fff" stroke="#b99ad8"/></svg><div class="product-img" style="background:#2e3b63" role="img" aria-label="Marinblå stövel"></div><div class="product-name">Stövlar</div><div class="product-sub">Vintage lätt sko</div><div class="product-price">325kr<s>450kr</s></div></article>
  </div>
  <div class="dots" style="margin-top:18px"><span class="dot dot--on">1</span><span class="dot">2</span></div>

  <div class="rule" style="margin:40px 0 0"></div>
  <h2 class="section-title" style="margin-top:30px"><span>News</span></h2>
  <section class="news" style="margin:18px 0 0;padding:12px 26px 0;height:120px">
    <div class="news-date">21 Maj 2018</div>
    <p class="news-text">Nya säsongen är här med lätta sneakers, sandaler och klackskor i vårens färger. Fri frakt och fri retur på alla beställningar.</p>
    <div class="news-icon" role="img" aria-label="Nyhetsikon"></div>
    <span class="arrow arrow--l" style="left:4px;top:36px"><svg viewBox="0 0 8 8"><path d="M5 1L2 4l3 3" stroke="#fff" fill="none"/></svg></span>
    <span class="arrow arrow--r" style="right:4px;top:36px"><svg viewBox="0 0 8 8"><path d="M3 1l3 3-3 3" stroke="#fff" fill="none"/></svg></span>
  </section>

  <div class="rule" style="margin:30px 0 0"></div>
  <h2 class="section-title" style="margin-top:30px"><span>Favorites</span></h2>
  <div class="framed" style="margin:22px 12px 0;height:150px">
    <div class="frame" style="left:30px;top:0;right:0;bottom:40px"></div>
    <div class="photo-run" role="img" aria-label="Person som knyter vita sneakers" style="position:absolute;left:0;top:16px;right:16px;bottom:0"></div>
  </div>
  <div class="framed" style="margin:44px 12px 0;height:134px">
    <div class="frame frame--black" style="left:30px;top:0;right:0;bottom:40px"></div>
    <div class="photo-sea" role="img" aria-label="Färgglada skor på turkos bakgrund" style="position:absolute;left:0;top:16px;right:16px;bottom:0"></div>
  </div>

  <nav class="foot-nav" style="grid-template-columns:repeat(3,1fr);margin:45px 14px 0;gap:10px">
    <a>Hem</a><a>Om oss</a><a>Produkter</a><a>Kategorier</a><a>Favoriter</a><a>Nyheter</a><a>Kontakt</a>
  </nav>
  <div class="brands" style="flex-direction:column;gap:26px;margin-top:50px">
    <span class="brand"><i></i>Arvena</span><span class="brand">Solvik</span><span class="brand">TAVIK</span><span class="brand">Mudlo</span>
  </div>

  <section class="newsletter" style="margin-top:60px;height:400px;padding-top:14px;background:var(--white)">
    <div class="nl-ghost" style="font-size:22px;margin-left:-20px">Newsletter Subscribe</div>
    <div class="nl-title" style="top:20px;font-size:10px">Subscribe Newsletter</div>
    <div class="nl-input" style="width:220px;margin-top:20px">E-post</div>
    <div class="features" style="flex-direction:column;align-items:center;gap:10px;margin-top:16px;background:var(--soft);padding:14px 0">
      <div class="feature" style="width:200px;height:80px"><svg viewBox="0 0 24 24"><circle cx="12" cy="10" r="6" fill="none" stroke="#5b1a9a" stroke-width="1.5"/><path d="M8 15l-2 7 6-3 6 3-2-7" fill="none" stroke="#5b1a9a" stroke-width="1.5"/></svg>30 dagars öppet köp</div>
      <div class="feature" style="width:200px;height:80px"><svg viewBox="0 0 24 24"><path d="M2 5h4l3 10h10l2-7H7" fill="none" stroke="#5b1a9a" stroke-width="1.5"/><circle cx="10" cy="19" r="1.5" fill="#5b1a9a"/><circle cx="17" cy="19" r="1.5" fill="#5b1a9a"/></svg>Fri frakt och fri retur</div>
      <div class="feature" style="width:200px;height:80px"><svg viewBox="0 0 24 24"><rect x="3" y="8" width="18" height="13" fill="none" stroke="#5b1a9a" stroke-width="1.5"/><path d="M3 8l4-5h10l4 5M12 3v18" fill="none" stroke="#5b1a9a" stroke-width="1.5"/></svg>Prisgaranti</div>
    </div>
  </section>

  <footer class="footer" style="height:285px;margin-top:0">
    <div class="footer-top" style="justify-content:space-between;padding:10px 10px 6px"><span>☏ +46 8 555 0142</span><span>✉ kundtjanst@kelvaro.se</span></div>
    <div style="padding:12px 10px 0;display:flex;flex-direction:column;gap:14px">
      <div><h4>CONTACT US</h4>Skovägen 12, Kelvaro AB<br>411 08 Göteborg<br>Telefon: +46 8 555 0142<br>E-post: kundtjanst@kelvaro.se</div>
      <div><h4>USEFUL LINKS</h4>Vanliga frågor<br>Leveransvillkor<br>Retur &amp; byte<br>Storleksguide</div>
      <div><h4>FOLLOW US</h4><div class="socials"><span></span><span></span><span></span></div></div>
    </div>
  </footer>
  <div class="copyright" style="padding:12px 8px">© 2018 Kelvaro AB · Integritetspolicy · Villkor · Cookies</div>
</main>

</body>
</html>
```